Business card

We need a business card design for our company based in Auckland , New Zealand called 'Kestrel + Design Ltd'. We provide architectural services. We would like to see designs that use the max. three colours (such as white, black, grey) The final design should communicate financial safety and growth."
Also I will provide our company logo. I would like to the logo to be embeded onto our business card.

Target Market(s)

new residential house, alteration & addition & light commericila design & drafting service

Industry/Entity Type

Architecture

Contact Information for Business Card

Company name: kestrel + design Ltd.
Name: Mark Telford
Job title: architectural designer & Design RQC
email address: mark@kdstudio.co.nz
mobile number: 02 5319 6620
web site: www.kdstudio.co.nz

Requirements
Must have
• My project must have..
• - embeded logo (attached company logo)
• I don't have a bigger version for our company logo, but I have one old one, so you can remove the word from it)
• - insert the attached small PDGQ logo & RQC logo
• - creative, simple and clear business card.
• - Max. three colours
Nice to have
• - Here are the samples I would like to share with you: http://www.velmorindex.com/blog/minimalistic-business-card-designs/
• I would like to have my business card like one of the creation.
Should not have
• TBA

```html
<!DOCTYPE html>
<html lang="en">
<head>
<meta charset="utf-8">
<title>Kestrel + Design Ltd — Business Card</title>
<link rel="stylesheet" href="https://fonts.googleapis.com/css2?family=Montserrat:wght@300;400;600;700&display=swap">
<style>
  :root {
    --backdrop: #858585;
    --card: #eaeae8;
    --ink: #1a1a1a;
    --ink-soft: #555555;
    --badge: #2a2a2a;
    --badge-light: #7a7a7a;
  }
  * { margin: 0; padding: 0; box-sizing: border-box; }
  html, body {
    width: 1105px;
    height: 1200px;
    overflow: hidden;
    background: var(--backdrop);
    font-family: "Montserrat", Arial, sans-serif;
    color: var(--ink);
  }
  .card {
    position: absolute;
    left: 182px;
    width: 746px;
    height: 424px;
    background: var(--card);
  }
  .card--front { top: 120px; }
  .card--back { top: 637px; }

  .holder-name {
    position: absolute;
    left: 46px;
    top: 40px;
    font-size: 26px;
    font-weight: 700;
    letter-spacing: 0.5px;
    text-transform: uppercase;
  }
  .holder-role {
    position: absolute;
    left: 46px;
    top: 76px;
    font-size: 20px;
    font-weight: 300;
    line-height: 28px;
    color: var(--ink-soft);
  }
  .company-name {
    position: absolute;
    left: 46px;
    top: 142px;
    font-size: 20px;
    font-weight: 300;
    color: var(--ink-soft);
  }
  .contact-list {
    position: absolute;
    left: 46px;
    top: 186px;
    list-style: none;
  }
  .contact-list li {
    display: flex;
    align-items: center;
    height: 29.5px;
    font-size: 19px;
    font-weight: 300;
    color: var(--ink-soft);
  }
  .contact-list svg {
    width: 18px;
    height: 18px;
    margin-right: 11px;
    flex: none;
  }
  .credential-badge {
    position: absolute;
    left: 49px;
    top: 326px;
    width: 76px;
    height: 76px;
    border-radius: 50%;
    background: var(--badge);
  }
  .association-badge {
    position: absolute;
    left: 152px;
    top: 338px;
    width: 122px;
    height: 48px;
    background: var(--badge-light);
  }
  .brand-mark {
    position: absolute;
    right: 40px;
    top: 326px;
    display: flex;
    align-items: center;
    gap: 10px;
    font-size: 18px;
    font-weight: 600;
    color: var(--ink);
  }
  .brand-mark__dot {
    width: 22px;
    height: 22px;
    border-radius: 50%;
    border: 3px solid var(--ink);
  }
  .back-url {
    position: absolute;
    left: 0;
    right: 0;
    top: 198px;
    text-align: center;
    font-size: 24px;
    font-weight: 700;
    letter-spacing: 4.5px;
    text-transform: uppercase;
  }
</style>
</head>
<body>
  <section class="card card--front">
    <h1 class="holder-name">Mark Telford</h1>
    <p class="holder-role">architectural designer<br>&amp; Design RQC</p>
    <p class="company-name">kestrel + design Ltd.</p>
    <ul class="contact-list">
      <li>
        <svg viewBox="0 0 18 18" aria-hidden="true"><rect x="4.5" y="1" width="9" height="16" rx="1.5" fill="none" stroke="#1a1a1a" stroke-width="2"/><rect x="7.5" y="13.5" width="3" height="1.5" fill="#1a1a1a"/></svg>
        02 5319 6620
      </li>
      <li>
        <svg viewBox="0 0 18 18" aria-hidden="true"><rect x="1.5" y="4" width="15" height="10" fill="#1a1a1a"/><path d="M1.5 4 L9 10 L16.5 4" fill="none" stroke="#eaeae8" stroke-width="1.3"/></svg>
        mark@kdstudio.co.nz
      </li>
      <li>
        <svg viewBox="0 0 18 18" aria-hidden="true"><circle cx="9" cy="9" r="7.5" fill="#1a1a1a"/><path d="M5 6 Q8 5 8 8 Q7 10 9 12 M11 4 Q13 7 12 9" fill="none" stroke="#eaeae8" stroke-width="1.3"/></svg>
        www.kdstudio.co.nz
      </li>
    </ul>
    <div class="credential-badge" role="img" aria-label="RQC credential badge"></div>
    <div class="association-badge" role="img" aria-label="PDGQ association badge"></div>
    <div class="brand-mark">
      <span class="brand-mark__dot"></span>
      <span>kestrel + design</span>
    </div>
  </section>

  <section class="card card--back">
    <p class="back-url">www.kdstudio.co.nz</p>
  </section>
</body>
</html>
```